Business card for Eyelash extension salon in MARLOW HEIGHTS,California USA

We need new business card for our salon in MARLOW HEIGHTS. The salon name is 'Lumarra' . We would like to have...Business name: Lumarra Name of person: will provide later Address 6128 N.Corbel Ridge Blvd MARLOW HEIGHTS , CA 90210 Phone: will provide later (Text only) Web: www.lumarrastudio-example.com Pictogrid icon, Friendvale icon follow us for seasonal campaign and news @lumarrastudioexample Design should look elegant, high-end, clean, simple, cohesive with my brand. Please refer my brand board. Business name color will be metallic bronzy color. Im thinking grey background or white background. Thanks

Target Market(s)

25-35. Gender neutral. People who are in Entertainment business industry.
This is High-end Eyelash extension salon in MARLOW HEIGHTS

Industry/Entity Type

Beauty Salon

Contact Information for Business Card

Business name: Lumarra
Name of person: will provide later
Address 6128 N.Corbel Ridge Blvd MARLOW HEIGHTS , CA 90210
Phone: will provide later (Text only)
Web: www.lumarrastudio-example.com
Pictogrid icon, Friendvale icon
follow us for seasonal campaign and news @lumarrastudioexample

Requirements
Must have
• Beautiful, elegant, clean and simple look but very attractive and modern
Should not have
• We don't like too clutter, too busy designs.

```html
<!DOCTYPE html>
<html lang="en">
<head>
<meta charset="utf-8">
<title>Lumarra — Business Card</title>
<link rel="stylesheet" href="https://fonts.googleapis.com/css2?family=Arimo:wght@400&family=Josefin+Sans:wght@300;400&display=swap">
<style>
  :root {
    --page: #ffffff;
    --espresso: #2f2621;
    --espresso-deep: #221b17;
    --espresso-edge: #1a1411;
    --bronze: #d4b391;
    --tan: #8b6b58;
    --ink-light: #ffffff;
    --ink-soft: #eee6df;
    --ink-muted: #8c8681;
    --photo-plant: #dfe3e0;
    --photo-room: #c9c6c1;
    --photo-fashion: #c7a58b;
  }
  * { box-sizing: border-box; margin: 0; padding: 0; }
  html, body {
    width: 1027px; height: 1200px; overflow: hidden;
    background: var(--page);
  }
  .canvas { position: relative; width: 1027px; height: 1200px; }

  .card {
    position: absolute; left: 18px; width: 991px; height: 565px;
    overflow: hidden;
    background: radial-gradient(ellipse at 45% 35%, var(--espresso) 0%, var(--espresso-deep) 75%, var(--espresso-edge) 100%);
  }
  .card-front { top: 25px; }
  .card-back { top: 609px; }

  .brand-name {
    position: absolute; left: 0; right: 0; top: 195px;
    text-align: center; color: var(--bronze);
    font-family: "Josefin Sans", sans-serif;
    font-size: 118px; font-weight: 300; letter-spacing: 6px; line-height: 1;
  }
  .brand-place {
    position: absolute; left: 446px; top: 380px;
    font-family: "Josefin Sans", sans-serif;
    font-size: 15px; font-weight: 400; letter-spacing: 4px;
    color: var(--ink-soft); white-space: nowrap;
  }

  .back-art { position: absolute; inset: 0; }

  .person-name {
    position: absolute; left: 85px; top: 82px;
    font-family: "Arimo", sans-serif; font-size: 22px; color: var(--ink-muted);
  }
  .contact-list {
    position: absolute; left: 52px; top: 316px; list-style: none;
    font-family: "Arimo", sans-serif; font-size: 22px; line-height: 29px;
    color: var(--ink-light);
  }
  .contact-item { display: flex; align-items: flex-start; gap: 10px; min-height: 29px; }
  .contact-icon { width: 17px; height: 17px; margin-top: 6px; flex: none; }
  .follow-note {
    position: absolute; left: 52px; top: 476px;
    font-family: "Arimo", sans-serif; font-size: 22px; color: var(--ink-light);
  }
  .social-handle {
    position: absolute; left: 52px; top: 519px;
    display: flex; align-items: center; gap: 12px;
    font-family: "Arimo", sans-serif; font-size: 20px; color: var(--ink-light);
  }
  .social-dot {
    width: 26px; height: 26px; border-radius: 50%;
    border: 2px solid var(--ink-light);
  }
</style>
</head>
<body>
<main class="canvas">

  <section class="card card-front" aria-label="Card front">
    <div class="brand-name">Lumarra</div>
    <div class="brand-place">MARLOW HEIGHTS</div>
  </section>

  <section class="card card-back" aria-label="Card back">
    <svg class="back-art" viewBox="0 0 991 565" width="991" height="565">
      <rect class="tan-block" x="790" y="0" width="201" height="150" fill="var(--tan)"/>
      <polygon class="tan-band" points="0,504 560,504 590,565 0,565" fill="var(--tan)"/>

      <g fill="var(--espresso-edge)">
        <polygon points="538,139 624,-12 798,-12 884,139 798,290 624,290"/>
        <polygon points="538,428 624,277 798,277 884,428 798,579 624,579"/>
        <polygon points="803,278 893,112 1080,112 1170,278 1080,444 893,444"/>
      </g>
      <g fill="none" stroke="var(--tan)" stroke-width="3">
        <polygon points="548,139 629,-2 793,-2 874,139 793,280 629,280"/>
        <polygon points="548,428 629,287 793,287 874,428 793,569 629,569"/>
        <polygon points="813,278 898,122 1075,122 1160,278 1075,434 898,434"/>
      </g>

      <polygon role="img" aria-label="Photo: bright interior with a hanging macrame planter"
        points="552,139 631,0 791,0 870,139 791,278 631,278" fill="var(--photo-plant)"/>
      <polygon role="img" aria-label="Photo: light living room with sofa and fireplace"
        points="552,428 631,289 791,289 870,428 791,567 631,567" fill="var(--photo-room)"/>
      <polygon role="img" aria-label="Photo: fashion detail of a cream jacket and denim"
        points="817,278 900,125 1073,125 1156,278 1073,431 900,431" fill="var(--photo-fashion)"/>
    </svg>

    <p class="person-name">This is the name area</p>

    <ul class="contact-list">
      <li class="contact-item">
        <svg class="contact-icon" viewBox="0 0 20 20" aria-label="Address">
          <circle cx="10" cy="10" r="8.5" fill="none" stroke="#fff" stroke-width="1.6"/>
          <path d="M10 15 C7 11.5 6.5 10 6.5 8.5 A3.5 3.5 0 0 1 13.5 8.5 C13.5 10 13 11.5 10 15Z" fill="#fff"/>
          <circle cx="10" cy="8.5" r="1.3" fill="var(--espresso)"/>
        </svg>
        <span>6128, N.Corbel Ridge<br>Blvd Marlow Heights, CA 90488</span>
      </li>
      <li class="contact-item">
        <svg class="contact-icon" viewBox="0 0 20 20" aria-label="Website">
          <circle cx="10" cy="10" r="8.5" fill="none" stroke="#fff" stroke-width="1.6"/>
          <circle cx="10" cy="10" r="4.5" fill="none" stroke="#fff" stroke-width="1.2"/>
          <path d="M5.5 10H14.5M10 5.5V14.5" stroke="#fff" stroke-width="1.2"/>
        </svg>
        <span></span>
      </li>
      <li class="contact-item">
        <svg class="contact-icon" viewBox="0 0 20 20" aria-label="Email">
          <circle cx="10" cy="10" r="8.5" fill="none" stroke="#fff" stroke-width="1.6"/>
          <rect x="5.5" y="7" width="9" height="6" fill="none" stroke="#fff" stroke-width="1.2"/>
          <path d="M5.5 10H14.5" stroke="#fff" stroke-width="1.2"/>
        </svg>
        <span></span>
      </li>
      <li class="contact-item">
        <svg class="contact-icon" viewBox="0 0 20 20" aria-label="Phone">
          <circle cx="10" cy="10" r="8.5" fill="none" stroke="#fff" stroke-width="1.6"/>
          <rect x="7.5" y="5.5" width="5" height="9" rx="1" fill="none" stroke="#fff" stroke-width="1.2"/>
        </svg>
        <span></span>
      </li>
    </ul>

    <p class="follow-note">Follow us for seasonal campaign and news</p>

    <div class="social-handle">
      <span class="social-dot" aria-hidden="true"></span>
      <span>@lumarrastudioexample</span>
    </div>
  </section>

</main>
</body>
</html>
```